Business cards for Champion Suri Alpaca Breeder

I am a seed stock Suri Alpaca breeder. I am looking for a business card design that is tactile with my logo or part of my logo embossed or debossed. I am open to other ideas.
My logo is available in detailed and simplified version. To get a feel for my style visit my website velmorfieldfleece.com

Target Market(s)

Alpaca breeders

Industry/Entity Type

Alpaca / Livestock

Contact Information for Business Card

Logo, Dora Plume, VELMORandFIELD.com, Saint Louis, MO 314-555-0172

Colors
0054AA
0677BA
7BADD7
CADEEF
E8F1F8

Requirements
Must have
• use brand guide
Nice to have
• embossed or debossed, incorporating a simple plaid use complimentary colors in logo
Should not have
• cartoon alpacas

```html
<!DOCTYPE html>
<html lang="en">
<head>
<meta charset="utf-8">
<title>Velmor &amp; Field — Business Cards</title>
<link rel="stylesheet" href="https://fonts.googleapis.com/css2?family=Cormorant+Garamond:wght@400;500&family=Crimson+Text:wght@400&family=Parisienne&display=swap">
<style>
  :root {
    --backdrop: #d9d4cc;
    --card-dark-center: #3d3d40;
    --card-dark-edge: #1c1c1e;
    --card-light-center: #fbf9f3;
    --card-light-edge: #e6e0d2;
    --silver: #d8d6d0;
    --muted-grey: #77736c;
    --ink: #3a3a3a;
    --teal: #3d5d6a;
    --teal-soft: #8fa3ab;
    --rule-tan: #c9bfae;
    --ornament-tan: #b8a88f;
  }
  * { box-sizing: border-box; margin: 0; padding: 0; }
  html, body { width: 1200px; height: 900px; overflow: hidden; }
  body { background: var(--backdrop); position: relative; font-family: "Crimson Text", Georgia, serif; }

  .card {
    position: absolute;
    left: 290px;
    width: 620px;
    height: 354px;
    border-radius: 3px;
    box-shadow: 0 10px 26px rgba(0,0,0,0.28);
    overflow: hidden;
  }

  /* Front */
  .card-front {
    top: 50px;
    background: radial-gradient(ellipse at 50% 40%, var(--card-dark-center), var(--card-dark-edge) 85%);
  }
  .front-mark {
    position: absolute;
    left: 0; right: 0; top: 118px;
    text-align: center;
    font-family: "Cormorant Garamond", Georgia, serif;
    font-weight: 500;
    font-size: 54px;
    letter-spacing: 2px;
    color: var(--silver);
    white-space: nowrap;
  }
  .front-rule {
    position: absolute;
    left: 90px; right: 90px; top: 232px;
    height: 1px;
    background: var(--muted-grey);
  }
  .front-url {
    position: absolute;
    left: 0; right: 0; top: 250px;
    text-align: center;
    font-family: "Crimson Text", Georgia, serif;
    font-size: 20px;
    letter-spacing: 6px;
    color: var(--muted-grey);
    white-space: nowrap;
  }

  /* Back */
  .card-back {
    top: 480px;
    background: radial-gradient(ellipse at 60% 35%, var(--card-light-center), var(--card-light-edge) 90%);
  }
  .back-mark {
    position: absolute;
    left: 20px; top: 222px;
    width: 266px;
    text-align: center;
    font-family: "Cormorant Garamond", Georgia, serif;
    font-weight: 400;
    font-size: 31px;
    line-height: 1.1;
    color: var(--ink);
    white-space: nowrap;
  }
  .back-rule {
    position: absolute;
    left: 40px; top: 272px;
    width: 226px; height: 1px;
    background: var(--rule-tan);
  }
  .back-ornament {
    position: absolute;
    left: 95px; top: 286px;
    width: 116px; height: 8px;
    border-radius: 4px;
    background: linear-gradient(90deg, transparent, var(--ornament-tan), transparent);
  }
  .divider-ornament {
    position: absolute;
    left: 296px; top: 40px;
    width: 18px; height: 260px;
    border-radius: 9px;
    background: linear-gradient(180deg, var(--teal), var(--teal-soft));
    opacity: 0.55;
  }
  .contact {
    position: absolute;
    left: 345px; top: 52px;
    color: var(--ink);
  }
  .contact-name {
    font-family: "Parisienne", cursive;
    font-size: 38px;
    color: var(--teal);
    margin-bottom: 18px;
    white-space: nowrap;
  }
  .contact-list { list-style: none; font-size: 20px; line-height: 1.25; }
  .contact-list li { display: flex; align-items: flex-start; gap: 10px; margin-bottom: 6px; white-space: nowrap; }
  .contact-list svg { flex: none; width: 16px; height: 20px; margin-top: 3px; }
  .contact-list .no-icon { padding-left: 26px; margin-top: -6px; }
</style>
</head>
<body>

  <section class="card card-front" aria-label="Card front">
    <div class="front-mark">VELMOR &amp; FIELD</div>
    <div class="front-rule"></div>
    <div class="front-url">VELMORandFIELD.com</div>
  </section>

  <section class="card card-back" aria-label="Card back">
    <div class="back-mark">VELMOR &amp; FIELD</div>
    <div class="back-rule"></div>
    <div class="back-ornament" role="img" aria-label="Small decorative flourish"></div>

    <div class="divider-ornament" role="img" aria-label="Vertical decorative feathered arrow divider"></div>

    <div class="contact">
      <div class="contact-name">Dora Plume</div>
      <ul class="contact-list">
        <li>
          <svg viewBox="0 0 16 20" aria-hidden="true"><rect x="3" y="1" width="10" height="18" rx="2" fill="none" stroke="var(--ink)" stroke-width="1.4"/><line x1="7" y1="16" x2="9" y2="16" stroke="var(--ink)" stroke-width="1.4"/></svg>
          <span>314-555-0172</span>
        </li>
        <li>
          <svg viewBox="0 0 16 20" aria-hidden="true"><circle cx="8" cy="10" r="6.5" fill="none" stroke="var(--ink)" stroke-width="1.4"/><ellipse cx="8" cy="10" rx="2.8" ry="6.5" fill="none" stroke="var(--ink)" stroke-width="1"/><line x1="1.5" y1="10" x2="14.5" y2="10" stroke="var(--ink)" stroke-width="1"/></svg>
          <span>VELMORandFIELD.com</span>
        </li>
        <li>
          <svg viewBox="0 0 16 20" aria-hidden="true"><path d="M8 19 C3 12 2 10 2 7.5 A6 6 0 0 1 14 7.5 C14 10 13 12 8 19 Z" fill="none" stroke="var(--ink)" stroke-width="1.4"/><circle cx="8" cy="7.5" r="2" fill="var(--ink)"/></svg>
          <span>Alder Run Farm</span>
        </li>
        <li class="no-icon"><span>Maple Hollow, MO</span></li>
      </ul>
    </div>
  </section>

</body>
</html>
```